HALVERWOOD MARKSMAN SPORTS, A modern indoor gun range comfortable for anyone to visit.

Please note the attached "Operating Plan", and "Letter of Introduction" for more details on our operation.

What we are looking for is the overall feel and look of the website. A lot of the details in how many links, what links, etc we will have built later. It's more important we get the right color scheme, flow, feel, etc.

This is an indoor gun range in Colorado. We are looking to be the skyline putt of the gun industry. We want a website that is simple, but stylish. Our range is forward thinking and modern. Please see our logo attached.

Our indoor range will also have a small cafe that will sell coffee, mixed soda drinks, and made from scratch cinnamon rolls.

Our look will be lighter colors. We want to avoid anything that would seem aggressive. Simple is the key here. We love simple clean designs. Pixel harbor has a good look and feel to it. Something with the same feel would be great. Our logo is red and black; however, we don't want the website to be dominated by those colors. Blue is also a great color.

We need a landing page that can shrink to different sizes of screens.
No mobile format.
Contact page with email submission
Menu will only have a couple links. We are open to different formats. Skyline putts format is also a good design.

Possible links will include: Home, Membership, About Us, Contact Us, Classes, Cafe

Target Market(s)

Primary target is male 35-55 years old with some college or more.

Number of Pages Required

3 page

Font styles to use
Sans Serif

Colors

Designer to choose colors to be used in the design.

Requirements
Must have
• Page 1 Landing first page
• Page 2 Blog posts to give updates on building progress
• Page 3 About us (hours of operation, etc)

```html
<!DOCTYPE html>
<html lang="en">
<head>
<meta charset="utf-8">
<title>Halverwood Marksman Sports</title>
<link href="https://fonts.googleapis.com/css2?family=Poppins:wght@500;600;700&family=Open+Sans:wght@400;600;700&display=swap" rel="stylesheet">
<style>
:root{
  --blue:#0a5ad6;
  --blue-dark:#0548c0;
  --red:#e10b0b;
  --ink:#111;
  --text:#444;
  --muted:#666;
  --soft:#f4f4f4;
  --line:#e4e4e4;
  --footer:#161616;
  --white:#fff;
}
*{margin:0;padding:0;box-sizing:border-box}
html,body{width:1200px;height:3827px;overflow:hidden}
body{position:relative;font-family:"Open Sans",sans-serif;color:var(--text);background:var(--white)}
section,header,footer{position:absolute;left:0;width:1200px}
.h-display{font-family:"Poppins",sans-serif;font-weight:700;color:var(--ink);letter-spacing:-.5px}
.btn{position:absolute;display:flex;align-items:center;justify-content:center;font-size:13px;color:var(--white);text-transform:uppercase;background:var(--blue)}
.btn--red{background:var(--red)}

/* header */
.site-header{top:0;height:82px;border-top:3px solid var(--red);background:var(--white);border-bottom:1px solid var(--line)}
.brand{position:absolute;left:98px;top:18px;display:flex;align-items:center;gap:10px}
.brand__dot{width:40px;height:40px;border-radius:50%;border:4px solid var(--ink)}
.brand__name{font-family:"Open Sans",sans-serif;font-weight:700;font-size:14px;line-height:1.15;color:var(--ink);width:150px}
.main-nav{position:absolute;right:98px;top:28px;display:flex;gap:36px;font-size:13px;color:#333}
.main-nav a{text-decoration:none;color:inherit}
.main-nav .is-active{color:var(--red);font-weight:600;border-top:1px solid var(--red);border-bottom:1px solid var(--red);padding:2px 8px;margin-top:-3px}

/* hero */
.hero{top:82px;height:457px}
.hero__photo{position:absolute;inset:0;background:linear-gradient(90deg,#050505 0%,#1d1a18 30%,#5e5148 55%,#a89684 78%,#cdbfae 100%)}
.hero__title{position:absolute;left:97px;top:80px;font-family:"Poppins",sans-serif;font-weight:700;font-size:60px;line-height:58px;color:var(--white)}
.hero__title span{color:var(--red);display:block}
.hero__tag{position:absolute;left:98px;top:268px;font-size:15px;color:var(--white)}
.hero .btn{top:325px;height:42px;width:146px}

/* about */
.about{top:539px;height:535px}
.about__photo{position:absolute;left:98px;top:85px;width:489px;height:367px;background:linear-gradient(135deg,#3b4450,#8a8f96 50%,#c9c6c0)}
.about__title{position:absolute;left:611px;top:84px;font-size:35px}
.about__body{position:absolute;left:613px;top:156px;width:490px;font-size:13.3px;line-height:22px}
.about__body p+p{margin-top:22px}
.about .btn{left:613px;top:412px;width:146px;height:42px}

/* membership */
.membership{top:1074px;height:383px;background:var(--soft)}
.membership__title{position:absolute;left:98px;top:72px;font-size:35px}
.membership__lead{position:absolute;left:98px;top:128px;font-size:17px;color:#333}
.membership__fee{position:absolute;left:96px;top:152px;font-family:"Poppins",sans-serif;font-weight:700;font-size:44px;color:var(--blue)}
.membership__note{position:absolute;left:100px;top:222px;font-size:13px;color:#222}
.membership .btn{left:98px;top:274px;width:146px;height:42px}
.plan{position:absolute;top:80px;width:316px;height:238px;background:var(--white);border-bottom:3px solid var(--blue);box-shadow:0 0 4px rgba(0,0,0,.08)}
.plan--year{left:441px}.plan--month{left:784px}
.plan__head{height:66px;border-bottom:1px solid var(--line);padding:20px 22px 0}
.plan__name{font-family:"Poppins",sans-serif;font-weight:600;font-size:21px;color:var(--ink);line-height:24px}
.plan__sub{font-size:13px;color:#222}
.plan--month .plan__head{padding-top:10px}
.plan__rows{padding:18px 22px 0;font-size:13px;color:#333}
.plan__row{display:flex;height:29px}
.plan__row b{width:95px;font-weight:700;color:#222}
.plan__fine{color:var(--blue);line-height:19px;margin-top:1px}

/* band */
.band{top:1457px;height:275px;background:linear-gradient(160deg,#0a57d4 0%,#0b60e0 45%,#0550c8 100%);color:var(--white);text-align:center}
.band__title{font-family:"Poppins",sans-serif;font-weight:600;font-size:32px;margin-top:60px}
.band__kicker{margin-top:34px;font-size:17px;font-weight:600;display:flex;justify-content:center;align-items:center;gap:10px}
.band__kicker i{display:block;width:28px;height:1px;background:var(--white)}
.band__text{font-size:17px;line-height:27px;margin-top:10px}

/* classes */
.classes{top:1732px;height:352px;background:var(--soft)}
.lanes{position:absolute;left:98px;top:69px;width:659px;height:211px;background:var(--white);border-left:4px solid var(--blue);box-shadow:0 0 4px rgba(0,0,0,.08)}
.lanes__head{height:76px;border-bottom:1px solid var(--line);padding:14px 20px;font-size:17px;font-weight:700;color:var(--blue);line-height:26px}
.lanes__body{padding:10px 20px;font-size:13.5px;color:#333}
.lanes__body h4{font-size:16px;color:var(--ink);font-weight:600;margin-bottom:6px}
.lanes__body li{list-style:none;line-height:25px}
.lanes__body li::before{content:"• ";color:var(--red)}
.classes__title{position:absolute;left:784px;top:83px;font-size:35px}
.classes__text{position:absolute;left:785px;top:138px;width:320px;font-size:18px;line-height:27px;color:#555}
.classes .btn{left:785px;top:222px;width:146px;height:42px}

/* blogs */
.blogs{top:2084px;height:585px}
.blogs__title{position:absolute;width:100%;text-align:center;top:76px;font-size:35px}
.post{position:absolute;top:181px;width:316px;height:315px;background:#f7f7f7;box-shadow:0 1px 3px rgba(0,0,0,.08)}
.post__photo{height:186px}
.post__date{position:absolute;left:20px;top:0;width:46px;height:52px;background:var(--blue);color:var(--white);text-align:center;font-size:14px;line-height:18px;padding-top:6px}
.post__date b{display:block;font-size:18px;font-weight:700}
.post__title{font-family:"Poppins",sans-serif;font-weight:600;font-size:19px;color:var(--ink);padding:10px 20px 0}
.post__excerpt{padding:6px 20px;font-size:13px;line-height:23px;color:#555}
.post__excerpt em{font-style:normal;color:var(--red)}

/* cafe */
.cafe{top:2669px;height:487px;background:var(--soft)}
.cafe__photo{position:absolute;left:615px;top:0;width:585px;height:487px;background:linear-gradient(160deg,#2e2622,#6b4a32 45%,#b08058 75%,#3a2c25)}
.cafe__title{position:absolute;left:98px;top:62px;font-size:35px}
.cafe__text{position:absolute;left:98px;top:127px;width:450px;font-size:13px;line-height:22px;color:#444}
.cafe__text b{font-weight:600;color:#222}
.hours{position:absolute;left:98px;top:212px;width:486px;background:var(--white);border-left:4px solid var(--blue);box-shadow:0 0 4px rgba(0,0,0,.08)}
.hours__head{height:37px;padding:8px 24px;font-size:17px;font-weight:700;color:var(--blue);border-bottom:1px solid var(--line)}
.hours__row{display:flex;height:31px;align-items:center;border-bottom:1px solid var(--line);font-size:12px}
.hours__row:last-child{border-bottom:0}
.hours__row b{width:224px;padding-left:24px;color:#222}
.cafe .btn{left:98px;top:375px;width:146px;height:42px}

/* contact */
.contact{top:3156px;height:312px;background:linear-gradient(160deg,#0a57d4 0%,#0b60e0 45%,#0550c8 100%);color:var(--white);text-align:center}
.contact__title{font-family:"Poppins",sans-serif;font-weight:600;font-size:35px;margin-top:60px}
.contact__text{font-size:18px;line-height:27px;margin-top:10px}
.contact .btn{left:527px;top:201px;width:146px;height:40px;background:var(--white);color:#222}

/* footer */
.site-footer{top:3468px;height:359px;background:var(--footer);color:#ddd}
.footer-brand{position:absolute;left:92px;top:118px;display:flex;align-items:center;gap:12px}
.footer-brand__dot{width:64px;height:64px;border-radius:50%;border:5px solid var(--white)}
.footer-brand__name{font-weight:700;font-size:19px;line-height:1.2;color:var(--white);width:170px}
.fcol{position:absolute;top:62px;font-size:13.5px;line-height:25px}
.fcol h5{font-family:"Poppins",sans-serif;font-weight:600;font-size:18px;color:var(--white);margin-bottom:6px}
.fcol a{display:block;color:#ddd;text-decoration:none}
.fcol .is-active{color:var(--red)}
.fcol--links{left:413px}
.fcol--address{left:585px;width:210px}
.social{display:flex;gap:8px;margin-top:2px}
.social i{width:27px;height:27px;border-radius:50%;background:#2e74c8}
.social i:last-child{background:var(--red)}
.fcol--form{left:841px;width:259px}
.field{height:37px;background:var(--white);margin-bottom:7px;padding:9px 16px;font-size:13px;font-style:italic;color:#777}
.submit{height:37px;background:var(--red);color:var(--white);font-size:13px;display:flex;align-items:center;justify-content:center}
.copyright{position:absolute;left:98px;right:98px;top:312px;border-top:1px solid #3a3a3a;text-align:center;padding-top:22px;font-size:11.5px;color:#ccc}
</style>
</head>
<body>

<header class="site-header">
  <div class="brand"><span class="brand__dot"></span><span class="brand__name">HALVERWOOD MARKSMAN SPORTS</span></div>
  <nav class="main-nav">
    <a class="is-active" href="#">HOME</a><a href="#">ABOUT US</a><a href="#">MEMBERSHIP</a><a href="#">CLASSES</a><a href="#">BLOGS</a><a href="#">CAFE</a><a href="#">CONTACT US</a>
  </nav>
</header>

<section class="hero">
  <div class="hero__photo" role="img" aria-label="Two women wearing ear protection and safety glasses practising at an indoor shooting lane"></div>
  <h1 class="hero__title">Halverwood<span>Marksman</span>Sports</h1>
  <p class="hero__tag">Colorado's Finest Indoor Shooting Range</p>
  <a class="btn btn--red" style="left:98px">Membership</a>
  <a class="btn" style="left:257px">Contact Us</a>
</section>

<section class="about">
  <div class="about__photo" role="img" aria-label="Instructor guiding a woman aiming a pistol on the range"></div>
  <h2 class="h-display about__title">About Us</h2>
  <div class="about__body">
    <p>We plan to start a family run state of the art indoor shooting range that is safe. We will foster an environment that allows men and women to come by themselves, feel comfortable, and are confident regardless of their experience level. We will hire staff based on guest service skills to focus on their overall experience.</p>
    <p>Halverwood Marksman Sports will be first and foremost dedicated to providing top-notch customer service to all guests in a relaxed, friendly, and caring manner. We will utilize only the most advanced safety technology to ensure a safe environment for our guests.</p>
  </div>
  <a class="btn">Read More</a>
</section>

<section class="membership">
  <h2 class="h-display membership__title">Membership</h2>
  <p class="membership__lead">Memberships will be offered</p>
  <p class="membership__fee">$58 Initial Fee</p>
  <p class="membership__note">(Waived if signed up prior to opening)</p>
  <a class="btn">Sign Up</a>
  <div class="plan plan--year">
    <div class="plan__head"><div class="plan__name">YEARLY</div></div>
    <div class="plan__rows">
      <div class="plan__row"><b>Individual:</b>$300 a year</div>
      <div class="plan__row"><b>Dual:</b>$400 a year</div>
      <div class="plan__row"><b>Family:</b>$450 a year</div>
      <p class="plan__fine">(Children are included up to age 26, and they do not need to live at home)</p>
    </div>
  </div>
  <div class="plan plan--month">
    <div class="plan__head"><div class="plan__name">MONTH-MONTH</div><div class="plan__sub">(NO CONTRACT OR OBLIGATION)</div></div>
    <div class="plan__rows">
      <div class="plan__row"><b>Individual:</b>$30 a year</div>
      <div class="plan__row"><b>Dual:</b>$40 a year</div>
      <div class="plan__row"><b>Family:</b>$45 a year</div>
      <p class="plan__fine">(Children age up to 26, and they do not need to live at home)</p>
    </div>
  </div>
</section>

<section class="band">
  <h2 class="band__title">Members are allowed unlimited visits to the range</h2>
  <p class="band__kicker"><i></i>Special before Opening<i></i></p>
  <p class="band__text">For every year purchased in advanced an additional 3 months will be given<br>Gunsmith will provide basic gunsmith services</p>
</section>

<section class="classes">
  <div class="lanes">
    <div class="lanes__head">All lanes are first come first serve. The only reservations will be for founding members.</div>
    <div class="lanes__body">
      <h4>Fees:</h4>
      <ul>
        <li>$20 Lane Rental per day (no extra cost for additional people in 1 lane)</li>
        <li>$20 Unlimited gun rentals</li>
        <li>$10 Single gun rental</li>
      </ul>
    </div>
  </div>
  <h2 class="h-display classes__title">Our Classes</h2>
  <p class="classes__text">First Wednesday of every month we will open at 6 am and close regularly.</p>
  <a class="btn">Know More</a>
</section>

<section class="blogs">
  <h2 class="h-display blogs__title">Our Blogs</h2>
  <article class="post" style="left:98px">
    <div class="post__photo" role="img" aria-label="Smiling woman in safety glasses holding a pistol" style="background:linear-gradient(135deg,#b9a48f,#e2d8cc)"></div>
    <div class="post__date">23rd<b>May</b></div>
    <h3 class="post__title">Lorem Ipsum</h3>
    <p class="post__excerpt">Simply dummy text of the printing and type-setting industry. The &nbsp;when an unknown printer &nbsp; <em>+ More</em></p>
  </article>
  <article class="post" style="left:441px">
    <div class="post__photo" role="img" aria-label="Shooters with yellow ear protection aiming down range" style="background:linear-gradient(135deg,#3f463a,#8b8d78)"></div>
    <div class="post__date">23rd<b>May</b></div>
    <h3 class="post__title">Lorem Ipsum</h3>
    <p class="post__excerpt">Simply dummy text of the printing and type-setting industry. The &nbsp;when an unknown printer &nbsp; <em>+ More</em></p>
  </article>
  <article class="post" style="left:784px">
    <div class="post__photo" role="img" aria-label="Instructor and smiling student aiming a handgun together" style="background:linear-gradient(135deg,#5a5650,#a59c8e)"></div>
    <div class="post__date">23rd<b>May</b></div>
    <h3 class="post__title">Lorem Ipsum</h3>
    <p class="post__excerpt">Simply dummy text of the printing and type-setting industry. The &nbsp;when an unknown printer &nbsp; <em>+ More</em></p>
  </article>
</section>

<section class="cafe">
  <h2 class="h-display cafe__title">Our Cafe</h2>
  <p class="cafe__text">Café will sell a small <b>variety of coffee</b> and <b>mixed soda drinks</b>. It will also carry made from <b>scratch cinnamon rolls</b> sold on a first come basis until sold out daily.</p>
  <div class="hours">
    <div class="hours__head">Our open hours will be:</div>
    <div class="hours__row"><b>Monday to Thursday</b>10am to 8pm</div>
    <div class="hours__row"><b>Friday &amp; Saturday</b>9 am to 10pm</div>
    <div class="hours__row"><b>Sunday</b>CLOSED</div>
  </div>
  <a class="btn">Read More</a>
  <div class="cafe__photo" role="img" aria-label="Warm cafe interior with dark wood tables, red chairs and hanging pendant lights"></div>
</section>

<section class="contact">
  <h2 class="contact__title">Contact Us</h2>
  <p class="contact__text">We will have highly trained safety officers that are friendly and<br>focused on our guests' experience and safety.</p>
  <a class="btn">Contact Now</a>
</section>

<footer class="site-footer">
  <div class="footer-brand"><span class="footer-brand__dot"></span><span class="footer-brand__name">HALVERWOOD MARKSMAN SPORTS</span></div>
  <div class="fcol fcol--links">
    <h5>Quick Links</h5>
    <a class="is-active" href="#">Home</a><a href="#">About Us</a><a href="#">Membership</a><a href="#">Classes</a><a href="#">Blogs</a><a href="#">Cafe</a><a href="#">Contact Us</a>
  </div>
  <div class="fcol fcol--address">
    <h5>Address</h5>
    <p>Lorem ipsum dolor sit a consectetur adipiscing elit.<br>Phone: 000-000-0000<br>Email: hello@halverwoodrange.com</p>
    <h5 style="margin-top:10px">Follow Us</h5>
    <div class="social"><i></i><i></i><i></i><i></i></div>
  </div>
  <div class="fcol fcol--form">
    <h5>Contact Us</h5>
    <div class="field">Name</div>
    <div class="field">Email</div>
    <div class="submit">SUBMIT</div>
  </div>
  <p class="copyright">©2019 By Halverwood Marksman Sports .All rights reserved</p>
</footer>

</body>
</html>
```